We are in search of a new business card design for our business. We have a Mexican Grocery Store called Tortilla Grove Market, we would like to see that some have mexican design, but we are open to any type of designs.

Phone: to be announced
Fax: to be announced

Address is:
2415 Calloway Blvd
Millbrook, MD 21090

```html
<!DOCTYPE html>
<html lang="en">
<head>
<meta charset="utf-8">
<title>Tortilla Grove Market – Business Card</title>
<link href="https://fonts.googleapis.com/css2?family=Lato:wght@400;700;900&display=swap" rel="stylesheet">
<style>
  :root {
    --saffron: #fdb010;
    --chili: #e1251b;
    --ink: #1d1d1d;
    --paper: #ffffff;
    --backdrop: #e9e6e1;
  }
  * { box-sizing: border-box; margin: 0; padding: 0; }
  html, body { width: 1200px; height: 901px; overflow: hidden; }
  body {
    background: var(--backdrop);
    font-family: "Lato", sans-serif;
    display: flex;
    align-items: center;
    justify-content: center;
    gap: 40px;
  }
  .card {
    width: 540px;
    height: 309px;
    position: relative;
    overflow: hidden;
    box-shadow: 0 6px 18px rgba(0,0,0,.18);
  }
  .card-back { background: var(--saffron); }
  .card-front { background: var(--paper); }

  .brand-name {
    font-weight: 900;
    color: var(--chili);
    line-height: 1.05;
    display: flex;
    align-items: center;
    gap: 10px;
  }
  .brand-dot {
    width: 14px; height: 14px;
    border-radius: 50%;
    background: var(--chili);
    flex: none;
  }
  .card-back .brand-name {
    position: absolute;
    left: 50%; top: 42%;
    transform: translate(-50%, -50%);
    font-size: 40px;
    white-space: nowrap;
  }
  .card-back .web {
    position: absolute;
    left: 0; right: 0; bottom: 54px;
    text-align: center;
    color: var(--paper);
    font-size: 15px;
    letter-spacing: .5px;
  }

  .card-front .brand-name {
    position: absolute;
    left: 36px; top: 30px;
    font-size: 28px;
  }
  .rule {
    position: absolute;
    left: 36px; right: 36px; top: 98px;
    height: 1.5px;
    background: var(--chili);
  }
  .contact {
    position: absolute;
    left: 36px; top: 116px;
    list-style: none;
    font-size: 14px;
    color: var(--ink);
    line-height: 21px;
  }
  .contact li { display: flex; align-items: center; gap: 8px; }
  .contact svg { width: 12px; height: 12px; fill: var(--chili); flex: none; }
  .person {
    position: absolute;
    right: 36px; top: 116px;
    text-align: right;
  }
  .person-name { color: var(--chili); font-size: 24px; font-weight: 400; }
  .person-role { color: var(--ink); font-size: 14px; margin-top: 2px; }
  .address {
    position: absolute;
    right: 36px; top: 196px;
    text-align: right;
    font-size: 14px;
    font-style: normal;
    line-height: 19px;
    color: var(--ink);
  }
  .front-band {
    position: absolute;
    left: 0; bottom: 0;
    width: 100%; height: 70px;
  }
  .card-front .web {
    position: absolute;
    right: 36px; bottom: 8px;
    color: var(--paper);
    font-size: 14px;
    letter-spacing: .4px;
  }
</style>
</head>
<body>

  <section class="card card-back" aria-label="Card back">
    <div class="brand-name"><span class="brand-dot"></span>Tortilla Grove Market</div>
    <p class="web">www.tortillagrovemarket.com</p>
  </section>

  <section class="card card-front" aria-label="Card front">
    <div class="brand-name"><span class="brand-dot"></span>Tortilla Grove Market</div>
    <div class="rule"></div>

    <ul class="contact">
      <li>
        <svg viewBox="0 0 24 24"><path d="M6.6 10.8a15.1 15.1 0 0 0 6.6 6.6l2.2-2.2c.3-.3.7-.4 1-.2 1.1.4 2.3.6 3.6.6.6 0 1 .4 1 1V20c0 .6-.4 1-1 1A17 17 0 0 1 3 4c0-.6.4-1 1-1h3.5c.6 0 1 .4 1 1 0 1.3.2 2.5.6 3.6.1.3 0 .7-.2 1z"/></svg>
        410 555 0142
      </li>
      <li>
        <svg viewBox="0 0 24 24"><path d="M6 2h12v5H6zM4 8h16a2 2 0 0 1 2 2v7h-4v5H6v-5H2v-7a2 2 0 0 1 2-2zm4 9v3h8v-3z"/></svg>
        410 555 0143
      </li>
      <li>
        <svg viewBox="0 0 24 24"><path d="M2 5h20v14H2zm2 2v.5l8 5 8-5V7l-8 5z"/></svg>
        hello@tortillagrovemarket.com
      </li>
    </ul>

    <div class="person">
      <p class="person-name">Marco Rivera</p>
      <p class="person-role">Owner</p>
    </div>

    <address class="address">
      2415 Calloway Blvd<br>
      Millbrook, MD 21090
    </address>

    <svg class="front-band" viewBox="0 0 540 70" preserveAspectRatio="none" aria-hidden="true">
      <path d="M0 10 C120 30 220 50 300 70 L0 70 Z" fill="var(--chili)"/>
      <path d="M0 26 C110 40 190 52 250 62 C320 48 420 40 540 38 L540 70 L0 70 Z" fill="var(--saffron)"/>
    </svg>
    <p class="web">www.tortillagrovemarket.com</p>
  </section>

</body>
</html>
```